Business card and stationary for consulting business

We need business cards and matching stationary for professional consulting business for employment and human resources issues.
One of the CraftHive designers designed the logo with our company name.  Use the colors in the logo and may use light yellow as an accent color.
Add
Mara T. Vollen, J.D., LL.M.
485 E. Callister Lane
Winter Park, Florida  32789
407-555-0183
maravollenjd@quillpost.example

Industry/Entity Type
Business

```html
<!DOCTYPE html>
<html lang="en">
<head>
<meta charset="utf-8">
<title>Keelstone business card</title>
<link rel="stylesheet" href="https://fonts.googleapis.com/css2?family=Quicksand:wght@400;500&display=swap">
<style>
  :root {
    --backdrop: #e1e5e5;
    --card: #ffffff;
    --navy-blue: #1f75a0;
    --sky-blue: #55cdf2;
    --ink: #333333;
    --divider: #b9c4c9;
  }
  * { box-sizing: border-box; margin: 0; padding: 0; }
  html, body {
    width: 1200px; height: 900px; overflow: hidden;
    background: var(--backdrop);
    font-family: "Quicksand", sans-serif;
  }
  .stage {
    width: 1200px; height: 900px;
    display: flex; align-items: center; justify-content: center; gap: 50px;
  }
  .card {
    position: relative;
    width: 520px; height: 300px;
    background: var(--card);
    box-shadow: 0 6px 18px rgba(0,0,0,0.12);
    overflow: hidden;
  }
  .brand { display: flex; align-items: center; gap: 10px; }
  .brand-name {
    font-weight: 400; color: var(--navy-blue);
    letter-spacing: 0.5px; line-height: 1;
    white-space: nowrap;
  }
  .brand-tagline {
    border-left: 1px solid var(--divider);
    padding-left: 8px;
    color: var(--sky-blue);
    line-height: 1.15;
    white-space: nowrap;
  }

  /* Front */
  .front .name-block {
    position: absolute; left: 0; top: 14px;
    width: 262px; height: 250px;
    background: var(--navy-blue);
    padding: 22px 18px;
  }
  .front .person-name {
    color: #fff; font-weight: 400; font-size: 26px; line-height: 1.05;
  }
  .front .person-name span { display: block; font-size: 22px; }
  .front .brand { position: absolute; left: 282px; top: 22px; }
  .front .brand-name { font-size: 27px; }
  .front .brand-tagline { font-size: 9px; }
  .front .contact {
    position: absolute; left: 282px; top: 180px;
    list-style: none; font-size: 10px; color: var(--ink);
  }
  .front .contact li { display: flex; align-items: flex-start; gap: 9px; margin-bottom: 8px; line-height: 1.3; }
  .front .contact svg { flex: none; width: 11px; height: 11px; margin-top: 1px; }
  .front .accent-band {
    position: absolute; left: 270px; right: 0; bottom: 0; height: 14px;
    background: var(--sky-blue);
  }

  /* Back */
  .back .logo-block {
    position: absolute; left: 0; bottom: 0;
    width: 150px; height: 190px;
    background: var(--navy-blue);
  }
  .back .accent-band {
    position: absolute; left: 150px; right: 0; bottom: 0; height: 12px;
    background: var(--sky-blue);
  }
  .back .brand { position: absolute; left: 178px; top: 112px; }
  .back .brand-name { font-size: 38px; }
  .back .brand-tagline { font-size: 12px; }
</style>
</head>
<body>
<main class="stage">
  <section class="card front" aria-label="Business card front">
    <div class="name-block">
      <h1 class="person-name">Mara<span>T. Vollen, J.D., LL.M.</span></h1>
    </div>
    <div class="brand">
      <span class="brand-name">Keelstone</span>
      <p class="brand-tagline">Grow Revenue<br>Control Costs<br>Secure Margins</p>
    </div>
    <ul class="contact">
      <li>
        <svg viewBox="0 0 12 12" aria-hidden="true"><rect x="2.5" y="0.5" width="7" height="11" rx="1.5" fill="#333"/><rect x="3.8" y="2" width="4.4" height="6" fill="#fff"/></svg>
        <span>407-555-0183</span>
      </li>
      <li>
        <svg viewBox="0 0 12 12" aria-hidden="true"><path d="M6 0.5a4 4 0 0 1 4 4c0 3-4 7-4 7s-4-4-4-7a4 4 0 0 1 4-4z" fill="#333"/><circle cx="6" cy="4.5" r="1.4" fill="#fff"/></svg>
        <span>485 E. Callister Lane<br>Cedar Hollow, Florida 32950</span>
      </li>
      <li>
        <svg viewBox="0 0 12 12" aria-hidden="true"><rect x="0.5" y="2" width="11" height="8" fill="#333"/><path d="M0.8 2.4 6 6.6l5.2-4.2" stroke="#fff" fill="none" stroke-width="1"/></svg>
        <span>maravollenjd@quillpost.example</span>
      </li>
    </ul>
    <div class="accent-band"></div>
  </section>

  <section class="card back" aria-label="Business card back">
    <div class="logo-block"></div>
    <div class="brand">
      <span class="brand-name">Keelstone</span>
      <p class="brand-tagline">Grow Revenue<br>Control Costs<br>Secure Margins</p>
    </div>
    <div class="accent-band"></div>
  </section>
</main>
</body>
</html>
```